corwin's pastel

We are a family business based in sydney introducing a common brazilian street food into sydney cafes and restaurants.
what we provide are pastels which is a thinly crust pie with assorted fillings
we mainly focus on supplying cafes and restaurants but we do sell privately.
We have had a few cafes ask to stock our cards due to customer request. except we don't have any!! hence why we need you. : )
I have attached an image of our pastels which is just to give you an idea of what they look like.
Updates
I have just seen all the designs and am impressed by some of your work. I will have to sit with my parter later today and will hopefully have some more constructive feedback and a decision soon.
Hello designers,
Hello designers,
Target Market(s)
cafe's and restaurants
Industry/Entity Type
Business
Contact Information for Business Card
Corwin's pastel
joaquim 0468217094
corwinspastel@fernmail.example

```html
<!DOCTYPE html>
<html lang="en">
<head>
<meta charset="utf-8">
<title>Corwin's Pastel – Business Card Options</title>
<link rel="stylesheet" href="https://fonts.googleapis.com/css2?family=Macondo&family=Noto+Serif&family=Open+Sans:wght@700&display=swap">
<style>
  :root {
    --sheet: #ffffff;
    --amber: #bf7f12;
    --leather-dark: #3a1a0d;
    --leather-light: #7a3413;
    --cocoa-dark: #4a2416;
    --cocoa-light: #6a3822;
    --plum: #2e1414;
    --badge-ink: #1a1012;
    --badge-cocoa: #5e3420;
    --card-ink: #ffffff;
    --cup: #c9ccc6;
    --pie-warm: #f0c088;
    --pie-muted: #d4a585;
  }
  * { margin: 0; padding: 0; box-sizing: border-box; }
  html, body { width: 1200px; height: 960px; overflow: hidden; background: var(--sheet); }
  .sheet { position: relative; width: 1200px; height: 960px; }

  .option-badge {
    position: absolute; width: 68px; height: 68px; border-radius: 50%;
    color: #fff; font: 700 36px/68px "Open Sans", sans-serif; text-align: center;
  }
  .badge-1 { left: 254px; top: 28px; background: var(--amber); }
  .badge-2 { left: 872px; top: 28px; background: var(--badge-ink); }
  .badge-3 { left: 254px; top: 878px; background: var(--badge-cocoa); }
  .badge-4 { left: 872px; top: 878px; background: var(--badge-ink); }

  .card { position: absolute; width: 596px; height: 372px; overflow: hidden; color: var(--card-ink); }
  .card-amber   { left: 0;     top: 120px; background: var(--amber); }
  .card-leather { left: 600px; top: 120px; background: radial-gradient(ellipse at 60% 40%, var(--leather-light), var(--leather-dark)); }
  .card-cocoa   { left: 0;     top: 498px; height: 362px; background: linear-gradient(135deg, var(--cocoa-light), var(--cocoa-dark)); }
  .card-plum    { left: 600px; top: 498px; height: 362px; background: var(--plum); }

  .brand, .owner {
    position: absolute; top: 64px; font: 400 44px/1 "Macondo", cursive;
    white-space: nowrap;
  }
  .brand { left: 36px; }
  .owner { left: 384px; }

  .steam { position: absolute; left: 334px; top: 60px; width: 28px; height: 76px;
    border-radius: 14px; background: linear-gradient(180deg, rgba(255,255,255,0.5), rgba(255,255,255,0.08)); }
  .cups { position: absolute; left: 58px; top: 156px; width: 166px; height: 92px;
    border-radius: 40px; background: radial-gradient(ellipse at 50% 40%, #a9aca6, var(--cup) 55%, #eef0ea); }
  .pie { position: absolute; left: 236px; top: 138px; width: 260px; height: 128px;
    border-radius: 120px 120px 70px 70px; background: linear-gradient(180deg, #f6d5ac, var(--pie-warm)); }
  .card-leather .pie, .card-cocoa .pie, .card-plum .pie {
    background: linear-gradient(180deg, #e2bc9c, var(--pie-muted)); opacity: 0.9; }

  .contact {
    position: absolute; left: 14px; bottom: 24px; font: 400 20px/1 "Noto Serif", serif;
    letter-spacing: 0.5px; white-space: nowrap;
  }
  .contact .divider { font-weight: 700; padding: 0 1px; }
</style>
</head>
<body>
<main class="sheet">
  <div class="option-badge badge-1">1</div>
  <div class="option-badge badge-2">2</div>

  <section class="card card-amber">
    <p class="brand">Corwin's Pastel</p>
    <div class="steam" role="img" aria-label="Rising steam wisps"></div>
    <p class="owner">Joaquim</p>
    <div class="cups" role="img" aria-label="Two steaming coffee cups on saucers"></div>
    <div class="pie" role="img" aria-label="Golden crusted pie"></div>
    <p class="contact">corwinspastel@fernmail.example<span class="divider">|</span>Mob-0468217094</p>
  </section>

  <section class="card card-leather" role="img" aria-label="Brown leather texture background">
    <p class="brand">Corwin's Pastel</p>
    <div class="steam" role="img" aria-label="Rising steam wisps"></div>
    <p class="owner">Joaquim</p>
    <div class="cups" role="img" aria-label="Two steaming coffee cups on saucers"></div>
    <div class="pie" role="img" aria-label="Golden crusted pie"></div>
    <p class="contact">corwinspastel@fernmail.example<span class="divider">|</span>Mob-0468217094</p>
  </section>

  <section class="card card-cocoa" role="img" aria-label="Brown textured paper background">
    <p class="brand">Corwin's Pastel</p>
    <div class="steam" role="img" aria-label="Rising steam wisps"></div>
    <p class="owner">Joaquim</p>
    <div class="cups" role="img" aria-label="Two steaming coffee cups on saucers"></div>
    <div class="pie" role="img" aria-label="Golden crusted pie"></div>
    <p class="contact">corwinspastel@fernmail.example<span class="divider">|</span>Mob-0468217094</p>
  </section>

  <section class="card card-plum">
    <p class="brand">Corwin's Pastel</p>
    <div class="steam" role="img" aria-label="Rising steam wisps"></div>
    <p class="owner">Joaquim</p>
    <div class="cups" role="img" aria-label="Two steaming coffee cups on saucers"></div>
    <div class="pie" role="img" aria-label="Golden crusted pie"></div>
    <p class="contact">corwinspastel@fernmail.example<span class="divider">|</span>Mob-0468217094</p>
  </section>

  <div class="option-badge badge-3">3</div>
  <div class="option-badge badge-4">4</div>
</main>
</body>
</html>
```